Brochure required for international Sports event

We need an 8 page brochure designed for an international sports event to be hosted in Japan. We are a Travel Company providing packages for participants looking to travel to the event.
The brochure will feature information on the event as well as services our company can provide.
The Brochure is to be an 8 page A4 document in portrait layout.
The brochure needs to be provided both as a print ready document and digital brochure for emailing.
Brochure structure, copy, logo and imagery has been provided
As well as a example brochure design that we like for inspiration.
Link to icons - https://www.filevault-example.net/sh/kq3mzplr8wbtyoc/BBBxkTLmQ4pR7Hs2nW6vYbCgE?dl=0
Target Market(s)
Masters/Veterans Sports Participants
Industry/Entity Type
Travel
Colors
Designer to choose colors to be used in the design.
Look and feel
Each slider illustrates characteristics of the customer's brand and the style your logo design should communicate.

```html
<!DOCTYPE html>
<html lang="en">
<head>
<meta charset="utf-8">
<title>Skyhop – Global Veterans Games 2021 Brochure</title>
<link rel="stylesheet" href="https://fonts.googleapis.com/css2?family=Montserrat:ital,wght@0,400;0,500;0,700;0,800;1,800&display=swap">
<style>
  :root {
    --orange: #ff5a12;
    --dark: #3a3a3c;
    --grey: #8c8c8e;
    --light-grey: #d6d6d8;
    --paper: #ffffff;
    --text: #4a4a4a;
    --backdrop: #ececec;
  }
  * { box-sizing: border-box; margin: 0; padding: 0; }
  html, body { width: 800px; height: 1200px; overflow: hidden; }
  body {
    background: var(--backdrop);
    font-family: "Montserrat", sans-serif;
    color: var(--text);
    position: relative;
  }
  .page {
    position: absolute;
    width: 352px;
    height: 498px;
    background: var(--paper);
    overflow: hidden;
    box-shadow: 0 2px 6px rgba(0,0,0,0.15);
  }
  .page--cover { left: 32px; top: 90px; }
  .page--event { left: 418px; top: 90px; }
  .page--venues { left: 32px; top: 618px; background: linear-gradient(180deg, #dcdcdc, #bdbdbd); }
  .page--tours { left: 418px; top: 618px; }
  .page__shapes { position: absolute; inset: 0; width: 100%; height: 100%; }

  .brand {
    position: absolute;
    display: flex;
    align-items: center;
    gap: 4px;
    font-family: "Montserrat", sans-serif;
    font-weight: 800;
    color: var(--dark);
    letter-spacing: -0.5px;
  }
  .brand__dot { width: 10px; height: 10px; border-radius: 50%; background: var(--orange); }
  .brand--cover { left: 108px; top: 26px; font-size: 28px; }
  .brand--cover .brand__dot { width: 18px; height: 18px; background: #fff; }
  .brand--event { left: 18px; top: 336px; font-size: 15px; }
  .brand--corner { right: 22px; top: 20px; font-size: 18px; }

  .cover-title {
    position: absolute;
    right: 68px;
    top: 384px;
    text-align: right;
    color: #fff;
    font-weight: 800;
    font-style: italic;
    line-height: 1;
  }
  .cover-title__year { font-size: 22px; display: block; }
  .cover-title__name { font-size: 20px; display: block; margin-top: 1px; }
  .cover-title__place { font-size: 14px; display: block; margin-top: 10px; font-weight: 700; }
  .cover-title__dates { font-size: 18px; display: block; margin-top: 10px; }
  .cover-title sup { font-size: 10px; }

  .section-title {
    position: absolute;
    font-weight: 800;
    color: var(--orange);
    line-height: 1.05;
  }
  .section-title__lead { display: block; color: var(--grey); font-size: 14px; }
  .event-heading { left: 24px; top: 30px; font-size: 17px; }
  .kansai-heading { left: 24px; top: 176px; font-size: 15px; }
  .copy {
    position: absolute;
    left: 24px;
    width: 250px;
    font-size: 6.2px;
    line-height: 1.35;
    text-align: justify;
  }
  .copy p + p { margin-top: 6px; }
  .copy--event { top: 84px; }
  .copy--kansai { top: 196px; }

  .venues-heading { left: 26px; top: 44px; font-size: 16px; }
  .tours-heading { left: 27px; top: 102px; font-size: 16px; }
  .copy--tours { left: 27px; top: 136px; width: 300px; }
  .include-heading {
    position: absolute;
    left: 27px;
    top: 198px;
    font-weight: 800;
    font-size: 15px;
    color: var(--grey);
    padding-bottom: 4px;
    border-bottom: 1.5px solid var(--orange);
  }
  .include-list {
    list-style: none;
    position: absolute;
    left: 28px;
    top: 236px;
    width: 310px;
    display: grid;
    grid-template-columns: 60px 88px 84px 78px;
    row-gap: 14px;
    font-size: 6.4px;
  }
  .include-list li { padding-left: 8px; position: relative; line-height: 1.3; }
  .include-list li::before {
    content: "+";
    position: absolute;
    left: 0;
    top: -1px;
    color: var(--orange);
    font-weight: 700;
  }

  .image-slot { position: absolute; }
  .map-slot {
    left: 18px; top: 150px; width: 316px; height: 252px;
    background: linear-gradient(135deg, #3fa9e0 0%, #7cc24a 35%, #f1a23a 60%, #6b4bb0 80%, #e8457a 100%);
  }
</style>
</head>
<body>

  <!-- Cover -->
  <section class="page page--cover">
    <svg class="page__shapes" viewBox="0 0 440 622" preserveAspectRatio="none">
      <defs>
        <linearGradient id="gateTones" x1="0" y1="0" x2="0" y2="1">
          <stop offset="0" stop-color="#b8280e"/>
          <stop offset="0.55" stop-color="#e04a1c"/>
          <stop offset="1" stop-color="#6e6e70"/>
        </linearGradient>
      </defs>
      <polygon points="0,0 380,0 320,310 420,622 0,622" fill="url(#gateTones)" role="img" aria-label="Photo of a long tunnel of red shrine gates over a stone path"/>
      <polygon points="380,0 405,0 345,310 440,600 440,622 420,622 320,310" fill="var(--orange)"/>
      <polygon points="405,0 440,0 440,600 345,310" fill="var(--dark)"/>
    </svg>
    <div class="brand brand--cover"><span>Skyhop</span><span class="brand__dot"></span></div>
    <h1 class="cover-title">
      <span class="cover-title__year">2021 GLOBAL</span>
      <span class="cover-title__name">VETERANS GAMES</span>
      <span class="cover-title__place">KANSAI, JAPAN</span>
      <span class="cover-title__dates">14<sup>th</sup> to 30<sup>th</sup> MAY 2021</span>
    </h1>
  </section>

  <!-- Event & region -->
  <section class="page page--event">
    <svg class="page__shapes" viewBox="0 0 440 622" preserveAspectRatio="none">
      <polygon points="240,0 440,0 440,110" fill="var(--orange)"/>
      <polygon points="330,0 440,0 440,55" fill="var(--light-grey)"/>
      <rect x="0" y="365" width="440" height="257" fill="#c9d3c4" role="img" aria-label="Photo of a veteran runner in a yellow vest stretching on a track railing"/>
      <polygon points="440,170 330,500 440,520" fill="var(--orange)"/>
      <polygon points="240,530 440,520 440,600" fill="var(--dark)" opacity="0.85"/>
    </svg>
    <h2 class="section-title event-heading"><span class="section-title__lead">The Global</span>VETERANS GAMES</h2>
    <div class="copy copy--event">
      <p>The 2021 Global Veterans Games will be the 10th Edition of the Games and the first time it will be held in Asia. Since its inception in Toronto in 1985 the Global Veterans Games has grown to become the world's largest mass-participated international sports event.</p>
      <p>The 2021 Games will be held in the Kansai region in the west of Japan and will take place over 17 days from May 14 – 30. An estimated 50,000 participants will meet to play a total of 65 sports and explore this beautiful and alluring country.</p>
    </div>
    <h2 class="section-title kansai-heading">Kansai</h2>
    <div class="copy copy--kansai">
      <p>Kansai consists of seven prefectures and was formerly the political and cultural center of Japan for many centuries and includes the cities of Kyoto, Osaka, Nara and Kobe.</p>
      <p>The Kansai region is located in the center of the Japanese islands and is home to over 20 million people. The region is also host to a number of incredible sights including Osaka Castle, Fushimi Inari Shrine, Kinkaku-ji (the Golden Pavilion), Nara Deer Park, Dotonbori District Nishiki Markets and Arashiyama Bamboo Grove.</p>
    </div>
    <div class="brand brand--event"><span>Skyhop</span><span class="brand__dot"></span></div>
  </section>

  <!-- Venues -->
  <section class="page page--venues">
    <svg class="page__shapes" viewBox="0 0 440 622" preserveAspectRatio="none">
      <polygon points="0,0 200,0 0,90" fill="#e6e6e6"/>
      <polygon points="260,0 440,0 440,120" fill="#cfcfcf"/>
      <polygon points="150,622 440,480 440,622" fill="var(--dark)" opacity="0.8"/>
      <polygon points="0,555 0,622 380,622" fill="var(--orange)"/>
    </svg>
    <h2 class="section-title venues-heading">Venues</h2>
    <div class="brand brand--corner"><span>Skyhop</span><span class="brand__dot"></span></div>
    <div class="image-slot map-slot" role="img" aria-label="Colour-coded venue map of the Kansai prefectures listing the 35 sports and their host cities"></div>
  </section>

  <!-- Tour packages -->
  <section class="page page--tours">
    <svg class="page__shapes" viewBox="0 0 440 622" preserveAspectRatio="none">
      <polygon points="0,0 240,0 0,130" fill="#c4c4c6"/>
      <polygon points="0,0 150,0 0,70" fill="#dcdcde"/>
      <polygon points="0,350 220,460 440,370 440,622 0,622" fill="var(--orange)"/>
      <polygon points="0,465 220,485 440,440 440,622 0,622" fill="#5a5a70" role="img" aria-label="Photo of rows of colourful suitcases on airport luggage trolleys"/>
    </svg>
    <div class="brand brand--corner"><span>Skyhop</span><span class="brand__dot"></span></div>
    <h2 class="section-title tours-heading">Tour Packages</h2>
    <div class="copy copy--tours">
      <p>Working with Airline and local Accommodation, Travel and Tour partners we have crafted Tour Packages with quality hotels conveniently located to the various sports venues as well as transport links. As no trip to Japan is complete without a visit to Tokyo we have included Japan's capital and some of the major sights in the package.</p>
    </div>
    <h3 class="include-heading">Package Include:</h3>
    <ul class="include-list">
      <li>Flights</li>
      <li>Accommodation</li>
      <li>Breakfast daily</li>
      <li>Meet &amp; Greet, with bilingual hosts</li>
      <li>Bilingual Local Guides</li>
      <li>Transport</li>
      <li>Bullet Train</li>
      <li>Sightseeing</li>
    </ul>
  </section>

</body>
</html>
```